Tidy Lark Premier Cleaning Service , Inc wants to make the buck so make it happen = )

I need a postcard design for my cleaning company. I have full ownership and 15+ years experience. At this time we take care of residential clients as well as commercial clients. Mainly offices. I do plan to expand my business in the commercial aspect. My experience is that we compete with franchise companies and my company deliveries a higher quality of work.
I already have a logo designed which I would like to use. Basically we do high quality, detail oriented work not just the first time to get the client but years and years ahead.

Target Market(s)

Commercial Offices

Industry/Entity Type

Residential

Font styles to use
Serif
Sans Serif

Colors
9bcb3c
ec1f27
33a6d7
3075b4
f78f20

Requirements
Must have
• focusing on quality, reliability, wants to stand of the crowd
Nice to have
• anything that makes the sale
Should not have
• too much general cleaning company adds

```html
<!DOCTYPE html>
<html lang="en">
<head>
<meta charset="utf-8">
<title>Tidy Lark Premier Cleaning Service, Inc – Postcard</title>
<link rel="stylesheet" href="https://fonts.googleapis.com/css2?family=Arimo:wght@400;700&display=swap">
<style>
  :root {
    --red: #ec1f27;
    --blue: #33a6d7;
    --navy: #3075b4;
    --green: #9bcb3c;
    --orange: #f78f20;
    --ink: #2b2b2b;
    --body: #4a4a4a;
    --paper: #ffffff;
    --backdrop: #eef0f2;
  }
  * { box-sizing: border-box; margin: 0; padding: 0; }
  html, body {
    width: 1200px; height: 731px; overflow: hidden;
    background: var(--backdrop);
    font-family: "Arimo", Arial, sans-serif;
  }
  .postcard {
    position: absolute; left: 90px; top: 25px;
    width: 1020px; height: 680px;
    background: var(--paper);
    box-shadow: 0 4px 18px rgba(0,0,0,.12);
    overflow: hidden;
  }
  .swoosh { position: absolute; left: 0; top: 0; width: 1020px; height: 680px; }
  .services {
    position: absolute; left: 40px; top: 92px; width: 470px;
    color: var(--body); font-size: 12.5px; line-height: 1.5;
  }
  .section-title {
    color: var(--red); font-size: 20px; font-weight: 400;
    letter-spacing: .5px; text-align: center; margin-bottom: 8px;
  }
  .sub-title {
    color: var(--blue); font-size: 17px; font-weight: 400;
    letter-spacing: .5px; margin-bottom: 3px;
  }
  .task-list { margin-bottom: 14px; text-align: justify; }
  .clients { text-align: justify; }
  .gallery {
    position: absolute; left: 40px; top: 532px; width: 430px; height: 74px;
    background: linear-gradient(100deg, #5a2d1c 0%, #a2744c 35%, #c9a87e 55%, #3a6fb7 78%, #8fb7dc 100%);
    clip-path: polygon(0 40%, 55% 20%, 62% 0, 100% 0, 100% 55%, 55% 80%, 0 100%);
  }
  .brand {
    position: absolute; left: 40px; top: 628px;
    display: flex; align-items: center; gap: 10px;
  }
  .brand-mark { width: 20px; height: 20px; background: var(--green); }
  .brand-name { color: var(--navy); font-size: 19px; font-weight: 400; }
  .contact {
    position: absolute; left: 560px; top: 34px;
    color: var(--ink); font-size: 12.5px; line-height: 1.6; font-style: normal;
  }
  .contact-title { font-size: 16px; font-weight: 700; letter-spacing: .5px; margin-bottom: 4px; }
  .contact-line { font-weight: 700; }
  .postage {
    position: absolute; left: 880px; top: 26px; width: 110px; height: 84px;
    border: 1px solid var(--ink);
    display: flex; align-items: center; justify-content: center; text-align: center;
    font-size: 8px; line-height: 1.4; color: var(--ink);
  }
</style>
</head>
<body>
<main class="postcard">
  <svg class="swoosh" viewBox="0 0 1020 680" aria-hidden="true">
    <path d="M0 0 H545 C400 22 200 44 0 76 Z" fill="var(--red)"/>
    <path d="M455 680 C495 645 525 600 545 520 L545 600 C535 635 520 662 505 680 Z" fill="var(--red)"/>
  </svg>

  <section class="services">
    <h2 class="section-title">RESIDENTIAL CLEANING</h2>
    <h3 class="sub-title">ALL LIVING AREAS</h3>
    <p class="task-list">Remove all cobwebs - Clean ceiling fans, dust light fixtures - Clean light switch plates - Clean smudges from doors - Dust blinds, window sills - Dust picture frames, knick-knacks - Dust furniture - Vacuum upholstered furniture - Clean baseboards - Straighten up - Remove trash - Vacuum</p>
    <h3 class="sub-title">KITCHEN</h3>
    <p class="task-list">Remove cob-webs - Dust ceiling fans, light fixtures - Wipe cabinets and drawers exterior - Clean light switch plates - Remove smudges from doors - Clean blinds and window sills - Counters and backsplash cleaned and sanitized - Sink cleaned and sanitized - Microwave cleaned inside -</p>
    <h2 class="section-title">COMMERCIAL CLEANING</h2>
    <h3 class="sub-title">WE PROVIDE SERVICES TO:</h3>
    <p class="clients">Apartment Buildings • Professional Offices • Property Management Companies • Realtors • Financial Institutions / Banks • Hair Salons / Nail Salons / Spas</p>
  </section>

  <div class="gallery" role="img" aria-label="Collage of cleaned home interiors and a modern office building"></div>

  <div class="brand">
    <span class="brand-mark"></span>
    <span class="brand-name">Tidy Lark Premier Cleaning Service, Inc</span>
  </div>

  <address class="contact">
    <p class="contact-title">CONTACT US TODAY :</p>
    <p class="contact-line">P.O. BOX 5820</p>
    <p class="contact-line">EASTON GROVE, SC 29876</p>
    <p class="contact-line">TEL : 555-310-2748</p>
    <p class="contact-line">Email Us : hello@tidylarkclean.com</p>
  </address>

  <div class="postage">First Class Mail<br>US Postage<br>PAID<br>PERMIT NO.</div>
</main>
</body>
</html>
```